Harbor LunaVital & Equipments

I need to create full stationery design for the company; Business Card, Envelop, Letterheads, Calendar and email template.

Our company is specialized in the import and export of nutritional, pharmaceutical and cosmetics in addition to medical equipments.

These is no limitation on how to use colors within the design.

Target Market(s)

Global

Industry/Entity Type

Healthcare

Other font styles liked:
• a font close to logo. Letterhead body text to be different than the address text

Requirements
Nice to have
• We will have multiple locations so it is good to keep space for future addresses.
• Stationary requirements:
• Letterhead: A4
• Envelopes: 3 regular sizes : large, medium and small (i do not know the sizes)
• Colors: extracted from the logo

```html
<!DOCTYPE html>
<html lang="en">
<head>
<meta charset="utf-8">
<title>Harbor LunaVital &amp; Equipments – Stationery</title>
<link rel="stylesheet" href="https://fonts.googleapis.com/css2?family=Ubuntu:wght@500&family=Arimo:wght@400;700&display=swap">
<style>
:root{
  --blue:#29a8e0;
  --blue-soft:#8fd3f3;
  --navy:#1c2a6b;
  --ink:#333;
  --paper:#ffffff;
  --stage:#eceef0;
  --brand-font:'Ubuntu',sans-serif;
  --text-font:'Arimo',sans-serif;
}
*{margin:0;padding:0;box-sizing:border-box}
html,body{width:1200px;height:937px;overflow:hidden;background:var(--stage)}
.stage{position:relative;width:1200px;height:937px}
.sheet{position:absolute;background:var(--paper);overflow:hidden;box-shadow:0 1px 3px rgba(0,0,0,.12)}
.sheet svg.wave{position:absolute;inset:0;width:100%;height:100%}
.brand{font-family:var(--brand-font);font-weight:500;color:var(--blue);line-height:1.05;position:absolute}
.brand-mark{position:absolute;background:var(--navy);border-radius:3px}

/* letterhead */
.letterhead{left:185px;top:68px;width:385px;height:544px}
.letterhead .brand-mark{left:44px;top:24px;width:22px;height:22px}
.letterhead .brand{left:18px;top:52px;font-size:14px;width:160px}
.letter{position:absolute;left:36px;top:130px;width:260px;font-family:var(--text-font);font-size:4.6px;color:var(--ink);line-height:1.5}
.letter p{margin-bottom:8px}
.letter .strong{font-weight:700}
.signature{width:26px;height:12px;background:#d9d9d9;margin:4px 0 6px}
.letterhead .contact{position:absolute;right:14px;top:452px;text-align:right;font-family:var(--text-font);font-size:4.6px;color:#fff;line-height:2}

/* folder */
.folder{left:636px;top:40px;width:458px;height:576px}
.folder .brand-mark{left:136px;top:378px;width:70px;height:70px;border-radius:8px}
.folder .brand{left:26px;top:462px;font-size:30px;width:360px}
.folder .web{position:absolute;left:26px;top:552px;font-family:var(--text-font);font-size:9px;letter-spacing:2.6px;color:var(--ink)}

/* business cards */
.card-front{left:45px;top:658px;width:176px;height:100px}
.card-front .person{position:absolute;right:8px;top:12px;text-align:right;font-family:var(--text-font);color:var(--ink)}
.card-front .person b{display:block;font-size:6px}
.card-front .person span{font-size:4px;letter-spacing:.5px}
.card-front .contact{position:absolute;right:8px;top:32px;text-align:right;font-family:var(--text-font);font-size:3.6px;color:var(--ink);line-height:1.9}
.card-front .brand-mark{left:40px;top:64px;width:11px;height:11px}
.card-front .brand{left:8px;top:78px;font-size:6.5px;width:90px}
.card-back{left:45px;top:785px;width:176px;height:100px}
.card-back .brand-mark{left:30px;top:38px;width:14px;height:14px}
.card-back .brand{left:8px;top:56px;font-size:8px;width:110px}

/* envelopes */
.envelope-front{left:265px;top:671px;width:431px;height:209px}
.envelope-front .brand-mark{left:55px;top:22px;width:24px;height:24px}
.envelope-front .brand{left:14px;top:52px;font-size:15px;width:200px}
.envelope-back{left:737px;top:671px;width:414px;height:209px}
.flap{position:absolute;left:0;top:0;width:414px;height:72px;background:var(--blue);border-radius:0 0 22px 40px}
.flap .web{position:absolute;left:0;right:0;top:28px;text-align:center;font-family:var(--text-font);font-size:9.5px;letter-spacing:2.4px;color:#fff}
</style>
</head>
<body>
<main class="stage">

  <!-- Letterhead -->
  <section class="sheet letterhead">
    <svg class="wave" viewBox="0 0 385 544" aria-hidden="true">
      <defs>
        <linearGradient id="lhBlue" x1="0" y1="1" x2="1" y2="0">
          <stop offset="0" stop-color="#29a8e0"/><stop offset="1" stop-color="#1e9bd6"/>
        </linearGradient>
      </defs>
      <path d="M0 470 C140 440 300 400 385 330" fill="none" stroke="#bfe5f7" stroke-width="6"/>
      <path d="M60 544 C200 500 330 440 385 370 L385 544 Z" fill="url(#lhBlue)"/>
      <path d="M20 544 C170 510 320 460 385 395" fill="none" stroke="#d6eff9" stroke-width="2"/>
      <path d="M0 510 C150 480 310 420 385 350" fill="none" stroke="#7ccdf0" stroke-width="1.5"/>
    </svg>
    <span class="brand-mark"></span>
    <div class="brand">Harbor LunaVital &amp; Equipments</div>
    <div class="letter">
      <p>July 2, 2012</p>
      <p><span class="strong">Dear Client,</span><br>Quay House, 4 Tide St., Portmere</p>
      <p>We are pleased to confirm receipt of your recent order for clinical supplies and nutritional products. Our team has reviewed each item and arranged shipment from our main warehouse. You will receive tracking details within two working days, along with the full export documents and product certificates for your records. Please contact us with any questions.</p>
      <p style="margin-top:14px">We value our partnership and look forward to supporting your clinics with reliable equipment and care.</p>
      <p style="margin-top:20px">Our new catalogue of cosmetic and pharmaceutical lines is now available, and a sales advisor will visit next month to present samples. Special terms apply to orders placed before the end of the quarter, including free delivery to all registered locations. We thank you for your continued trust in our service and products.</p>
      <p>Best Regards,</p>
      <div class="signature" role="img" aria-label="Handwritten signature"></div>
      <p><span class="strong">Dara Venn</span><br>Director<br><br>Quay House, 4 Tide St., Portmere</p>
    </div>
    <div class="contact">
      12 Harbor Row<br>Seaside Road PRT<br>
      014 220 5180 &#9742;<br>014 220 5181 &#9742;<br>014 220 5182 &#9993;<br>
      info@harborlunavital.com<br>www.harborlunavital.com
    </div>
  </section>

  <!-- Folder -->
  <section class="sheet folder">
    <svg class="wave" viewBox="0 0 458 576" aria-hidden="true">
      <defs>
        <linearGradient id="fBlue" x1="0" y1="0" x2="0.4" y2="1">
          <stop offset="0" stop-color="#29a8e0"/><stop offset="0.6" stop-color="#bfe5f7" stop-opacity=".5"/><stop offset="1" stop-color="#29a8e0"/>
        </linearGradient>
      </defs>
      <path d="M70 0 L140 0 C180 170 340 260 458 300 L458 576 L452 576 C360 420 110 250 70 0 Z" fill="url(#fBlue)" opacity=".55"/>
      <path d="M70 0 C100 220 300 360 452 576" fill="none" stroke="#29a8e0" stroke-width="8"/>
      <path d="M92 0 C130 210 320 330 458 420" fill="none" stroke="#29a8e0" stroke-width="3"/>
      <path d="M115 0 C160 190 330 280 458 330" fill="none" stroke="#8fd3f3" stroke-width="2"/>
      <path d="M230 140 C300 260 400 360 458 400" fill="none" stroke="#d6eff9" stroke-width="14" opacity=".7"/>
    </svg>
    <span class="brand-mark"></span>
    <div class="brand">Harbor LunaVital &amp; Equipments</div>
    <div class="web">www.harborlunavital.com</div>
  </section>

  <!-- Business card front -->
  <section class="sheet card-front">
    <svg class="wave" viewBox="0 0 176 100" aria-hidden="true">
      <path d="M0 0 L70 0 C60 30 30 55 0 65 Z" fill="#29a8e0"/>
      <path d="M0 72 C40 58 70 30 84 0" fill="none" stroke="#8fd3f3" stroke-width="3"/>
      <path d="M0 80 C50 62 85 30 100 0" fill="none" stroke="#d6eff9" stroke-width="2"/>
    </svg>
    <div class="person"><b>ELIN MARSH</b><span>DIRECTOR</span></div>
    <div class="contact">12 Harbor Row<br>Seaside Road PRT<br>014 220 5180 &#9742;<br>014 220 5181 &#9742;<br>014 220 5182 &#9993;<br>info@harborlunavital.com</div>
    <span class="brand-mark"></span>
    <div class="brand">Harbor LunaVital &amp; Equipments</div>
  </section>

  <!-- Business card back -->
  <section class="sheet card-back">
    <svg class="wave" viewBox="0 0 176 100" aria-hidden="true">
      <path d="M140 0 C165 30 172 70 168 100 L176 100 L176 0 Z" fill="#1c2a6b"/>
      <path d="M128 0 C155 35 162 70 158 100" fill="none" stroke="#29a8e0" stroke-width="1.5"/>
    </svg>
    <span class="brand-mark"></span>
    <div class="brand">Harbor LunaVital &amp; Equipments</div>
  </section>

  <!-- Envelope front -->
  <section class="sheet envelope-front">
    <svg class="wave" viewBox="0 0 431 209" aria-hidden="true">
      <defs>
        <linearGradient id="eNavy" x1="0" y1="0" x2="1" y2="0">
          <stop offset="0" stop-color="#1c2a6b"/><stop offset="1" stop-color="#b9bfe0" stop-opacity=".3"/>
        </linearGradient>
      </defs>
      <path d="M255 0 L300 0 C330 40 380 70 431 80 L431 95 C360 80 290 40 255 0 Z" fill="url(#eNavy)"/>
      <path d="M258 0 C300 50 370 100 431 150" fill="none" stroke="#1c2a6b" stroke-width="3"/>
      <path d="M266 0 C310 60 380 120 431 180" fill="none" stroke="#3c4a8f" stroke-width="1.2"/>
    </svg>
    <span class="brand-mark"></span>
    <div class="brand">Harbor LunaVital &amp; Equipments</div>
  </section>

  <!-- Envelope back -->
  <section class="sheet envelope-back">
    <div class="flap"><div class="web">www.harborlunavital.com</div></div>
  </section>

</main>
</body>
</html>
```